Skin Care business card for esthetician that is home based

I need a business card for my esthetician business. I would like to use a picture provided.
I want the picture #1 that I have provided to be as the main background with my title and the moto underneath in smaller lettering. Below that as a seperate thing I would like my full name and underneath in small letters to say "esthetician".
As a seperate paragraph I would like my address then phone number, email and my website that I have provided in the business card details.
On the back side I would like my second picture to be small and in the top left corner and then have the "nice to haves" details to be at the center bottom of the card.
Target Market(s)
mosty women between 18 and 60 years old
Industry/Entity Type
Skin Care
Contact Information for Business Card
Velvet Bloom Skin Care - Main Title
Bringing out your natural glow - motto
Marisol Teodora Vinchek -
Phone: 314.827.5093
7382 SW 9th Avenue
Oakvale WA 98472
oakvaleskincare@mailhaven.example
www.oakvaleskincare.example
Must have
- Picure I provided or other similar photo.
Nice to have
- On the back side:
Bringing out your natural glow
www.oakvaleskincare.example

```html
<!DOCTYPE html>
<html lang="en">
<head>
<meta charset="utf-8">
<title>Velvet Bloom Skin Care — Business Card</title>
<link rel="stylesheet" href="https://fonts.googleapis.com/css2?family=Playfair+Display:wght@400&family=Open+Sans:wght@400&display=swap">
<style>
  :root {
    --backdrop: #cbaea9;
    --card-white: #ffffff;
    --blush: #fcefeb;
    --ink: #231f20;
    --photo-light: #fbe7e0;
    --photo-mid: #efd4c9;
    --photo-deep: #c9a393;
    --card-shadow: rgba(110, 80, 76, 0.45);
  }
  html, body {
    margin: 0;
    padding: 0;
    width: 1200px;
    height: 1200px;
    overflow: hidden;
    background: var(--backdrop);
  }
  .canvas {
    position: relative;
    width: 1200px;
    height: 1200px;
  }
  .card {
    position: absolute;
    left: 254px;
    width: 691px;
    height: 395px;
    box-shadow: 5px 5px 4px var(--card-shadow);
    overflow: hidden;
  }
  .card--front { top: 148px; }
  .card--back { top: 649px; background: var(--card-white); }

  .front-photo {
    position: absolute;
    inset: 0;
    background:
      radial-gradient(ellipse 120px 150px at 48% 30%, #f9e1d7 0%, rgba(249,225,215,0) 100%),
      radial-gradient(ellipse 200px 230px at 80% 55%, rgba(201,163,147,0.75) 0%, rgba(201,163,147,0) 100%),
      linear-gradient(100deg, var(--photo-mid) 0%, var(--photo-light) 45%, var(--photo-light) 65%, var(--photo-mid) 100%);
  }
  .front-content {
    position: absolute;
    inset: 0;
    text-align: center;
    color: var(--ink);
  }
  .brand-title {
    position: absolute;
    left: 0; right: 0;
    top: 199px;
    margin: 0;
    font-family: "Playfair Display", serif;
    font-weight: 400;
    font-size: 34px;
    letter-spacing: 0.13em;
    line-height: 1;
  }
  .brand-motto {
    position: absolute;
    left: 0; right: 0;
    top: 255px;
    margin: 0;
    font-family: "Playfair Display", serif;
    font-weight: 400;
    font-size: 22px;
    letter-spacing: 0.04em;
    line-height: 1;
  }
  .brand-web {
    position: absolute;
    left: 0; right: 0;
    top: 354px;
    margin: 0;
    font-family: "Open Sans", sans-serif;
    font-size: 19px;
    letter-spacing: 0.12em;
    line-height: 1;
  }

  .back-panel {
    position: absolute;
    left: 27px;
    top: 27px;
    width: 636px;
    height: 341px;
    background: var(--blush);
  }
  .portrait {
    position: absolute;
    left: 0;
    top: 0;
    width: 189px;
    height: 189px;
    background: linear-gradient(160deg, #a9a196 0%, #c8beb0 40%, #e8e6e2 70%, #6e6a68 100%);
  }
  .identity {
    position: absolute;
    left: 189px;
    right: 0;
    top: 0;
    height: 222px;
    text-align: center;
    color: var(--ink);
  }
  .identity-name {
    position: absolute;
    left: 0; right: 0;
    top: 90px;
    margin: 0;
    font-family: "Playfair Display", serif;
    font-weight: 400;
    font-size: 35px;
    line-height: 1.1;
  }
  .identity-role {
    position: absolute;
    left: 0; right: 0;
    top: 143px;
    margin: 0;
    font-family: "Open Sans", sans-serif;
    font-size: 20px;
    letter-spacing: 0.12em;
    line-height: 1;
  }
  .panel-divider {
    position: absolute;
    left: 0;
    right: 0;
    top: 222px;
    height: 1px;
    background: var(--card-white);
  }
  .contact {
    position: absolute;
    top: 251px;
    margin: 0;
    font-family: "Open Sans", sans-serif;
    font-size: 17px;
    letter-spacing: 0.12em;
    line-height: 31px;
    color: var(--ink);
    font-style: normal;
  }
  .contact--address { left: 27px; text-align: left; }
  .contact--reach { right: 26px; text-align: right; }
</style>
</head>
<body>
<main class="canvas">
  <section class="card card--front">
    <div class="front-photo" role="img" aria-label="Photo of a relaxing facial treatment with a candle and spa towels, softened in blush tones"></div>
    <div class="front-content">
      <h1 class="brand-title">VELVET BLOOM SKIN CARE</h1>
      <p class="brand-motto">Bringing out your natural glow</p>
      <p class="brand-web">WWW.OAKVALESKINCARE.EXAMPLE</p>
    </div>
  </section>

  <section class="card card--back">
    <div class="back-panel">
      <div class="portrait" role="img" aria-label="Portrait photo of the esthetician in a white treatment uniform"></div>
      <div class="identity">
        <h2 class="identity-name">Marisol Teodora Vinchek</h2>
        <p class="identity-role">ESTHETICIAN</p>
      </div>
      <div class="panel-divider"></div>
      <address class="contact contact--address">7382 SW 9th Avenue<br>Oakvale WA 98472</address>
      <address class="contact contact--reach">Phone: 314.827.5093<br>oakvaleskincare@mailhaven.example</address>
    </div>
  </section>
</main>
</body>
</html>
```